InnRiderz Web Temp | ||
Web Temp | ||
Transportation | ||
www.innriderz.example | ||
Inn Riderz provides transportation from the top hotels around the world to the airports and vice versa. | ||
I would like to see a clean website, which looks very professional and inspires confidence in the user that the service is outstanding. It needs to look good with our logo, which has been uploaded for your reference. I would like the designer to include the text at the bottom of the pdf file that was uploaded. Additionally, there should be an area on the site that states, "Book Hotels, Flights...." followed by a buttom and "powered by trovask" |
Professional Sophisticated Corporate Modern Elegant |
below header | ||
trovask.example | ||
global-gate-shuttle.example | ||
pelunta.example | ||
Similar to trovask and pelunta, the site needs to be engaging. Most importantly it needs to show the following drop down input fields. (1) Select a country (2) Select a city (3) Rountrip (followed by circle that users can select) (4) One Way (followed by circle that users can select) (5) Select Hotel (drop down menu) (6) Select airport (drop down menu) (7) Arriving/Departing (pop up calendar). I have uploaded another file with a very crude mock up. But the text at the bottom of that sample should be included. I would like the designer to include the text at the bottom of the pdf file that was uploaded. Additionally, there should be an area on the site that states, "Book Hotels, Flights...." followed by a buttom and "powered by trovask" |

```html
<!DOCTYPE html>
<html lang="en">
<head>
<meta charset="utf-8">
<title>Inn Riderz Booking</title>
<link href="https://fonts.googleapis.com/css2?family=Arimo:wght@400;700&display=swap" rel="stylesheet">
<style>
:root{
  --sky-top:#14406a;
  --sky-bottom:#2c6ea8;
  --page-dark:#353637;
  --page-mid:#4a4b4c;
  --panel-white:#ffffff;
  --panel-grey:#d9d9d9;
  --nav-text:#4a6f94;
  --nav-active:#2a7cc4;
  --label-blue:#1f6fb8;
  --ink:#1d1d1d;
  --heading-blue:#1d5f9c;
  --field-grey:#c9c9c9;
  --field-dark:#8d8d8d;
  --go-blue:#2f86d6;
  --photo-sky:#9fc6e6;
  --photo-car:#1e8fc9;
  --footer-text:#e6e6e6;
}
*{box-sizing:border-box;margin:0;padding:0}
html,body{width:1200px;height:874px;overflow:hidden}
body{
  position:relative;
  font-family:"Arimo",Arial,sans-serif;
  color:var(--ink);
  background:
    linear-gradient(180deg,var(--sky-top) 0,var(--sky-bottom) 170px,var(--page-mid) 172px,var(--page-dark) 260px,var(--page-dark) 100%);
}
.member-links{position:absolute;right:102px;top:10px;font-size:16px;color:#c9d9e8}
.member-links b{color:#fff;font-weight:400}

.site-nav{
  position:absolute;left:101px;top:43px;width:998px;height:77px;
  background:linear-gradient(180deg,#fdfdfd,#e4e8ec);
  border-radius:20px;box-shadow:0 3px 8px rgba(0,0,0,.35);
}
.site-nav a{position:absolute;top:28px;font-size:19px;color:var(--nav-text);text-decoration:none;white-space:nowrap}
.site-nav a.active{color:var(--nav-active);font-weight:700}

.brand-oval{
  position:absolute;left:458px;top:12px;width:272px;height:134px;border-radius:50%;
  background:radial-gradient(ellipse at 50% 40%,#ffffff 55%,#dde3ea 100%);
  box-shadow:0 4px 10px rgba(0,0,0,.35);
  display:flex;align-items:center;justify-content:center;gap:10px;
}
.brand-mark{width:22px;height:22px;border-radius:50%;background:var(--heading-blue)}
.brand-name{font-size:27px;font-weight:700;color:var(--heading-blue);white-space:nowrap}

.booking-panel{position:absolute;left:101px;top:175px;width:446px;height:598px;background:var(--panel-white)}
.booking-title{position:absolute;left:10px;top:18px;font-size:34px;font-weight:400;color:#111}
.booking-rule{position:absolute;left:10px;right:10px;top:63px;border-top:1px solid #ccc}
.field-label{position:absolute;font-size:16px;color:var(--label-blue);text-transform:uppercase}
.select-box{
  position:absolute;width:175px;height:36px;border-radius:5px;
  background:linear-gradient(180deg,#e3e3e3,var(--field-grey));
  border:1px solid #aaa;font-size:15px;color:#6d6d6d;padding:9px 10px;
}
.select-box::after{
  content:"";position:absolute;right:3px;top:3px;width:24px;height:28px;border-radius:4px;
  background:linear-gradient(180deg,#a3a3a3,var(--field-dark));
}
.select-box svg{position:absolute;right:9px;top:13px;z-index:1}
.check-box{position:absolute;width:26px;height:17px;border-radius:3px;background:linear-gradient(180deg,#ececec,#bdbdbd);border:1px solid #999}
.go-button{
  position:absolute;left:264px;top:437px;width:156px;height:44px;border-radius:8px;
  background:linear-gradient(180deg,#6fb6f2,var(--go-blue) 55%,#1f65a8);
  border:2px solid #aacff0;color:#fff;font-size:17px;text-align:right;padding:11px 22px;
}
.panel-divider{position:absolute;left:10px;right:10px;top:520px;border-top:1px solid #ddd}
.social-chip{position:absolute;top:534px;width:29px;height:29px;border-radius:4px;background:#b8b8b8}
.phone-box{
  position:absolute;left:187px;top:535px;width:250px;height:36px;background:#1a1a1a;
  color:#fff;font-size:25px;letter-spacing:3px;padding:4px 0 0 44px;white-space:nowrap;
}
.phone-box svg{position:absolute;left:12px;top:8px}

.promo-panel{position:absolute;left:559px;top:175px;width:540px;height:598px;background:var(--panel-grey)}
.promo-title{position:absolute;left:9px;top:12px;font-size:19px;font-weight:700;color:var(--heading-blue)}
.slide-arrows{position:absolute;right:12px;top:10px;display:flex;gap:4px}
.slide-arrows span{width:24px;height:24px;border-radius:50%;background:#fff;border:1px solid #aaa;font-size:12px;text-align:center;line-height:22px;color:#555}
.promo-photo{
  position:absolute;left:7px;top:41px;width:528px;height:331px;
  background:linear-gradient(180deg,var(--photo-sky) 0,#7eaed1 45%,var(--photo-car) 70%,#1a5e8e 100%);
}
.slide-dots{position:absolute;right:14px;top:358px;display:flex;gap:4px}
.slide-dots i{width:10px;height:10px;border-radius:50%;background:#e8e8e8;border:1px solid #888}
.slide-dots i.on{background:#2a7cc4}
.promo-copy{position:absolute;left:9px;width:515px;font-size:18px;line-height:21px;letter-spacing:.6px;color:#1a1a1a}

.newsletter{position:absolute;left:101px;top:787px;width:230px;height:34px;background:#fff;font-size:14px;color:#888;padding:9px 8px}
.subscribe-button{position:absolute;left:221px;top:821px;width:110px;height:24px;background:#111;color:#fff;font-size:15px;text-align:center;line-height:24px}
.footer-brand{position:absolute;left:490px;top:800px;display:flex;align-items:center;gap:8px;opacity:.45}
.footer-brand .brand-mark{width:18px;height:18px;background:#aaa}
.footer-brand .brand-name{font-size:24px;color:#aaa}
.copyright{position:absolute;right:102px;top:808px;font-size:12px;color:var(--footer-text)}
</style>
</head>
<body>

<div class="member-links">Already a memmber | <b>sign in</b></div>

<nav class="site-nav">
  <a class="active" style="left:32px">Home</a>
  <a style="left:110px">About Us</a>
  <a style="left:224px">Services</a>
  <a style="left:645px">Cusstomer Care</a>
  <a style="left:822px">Group</a>
  <a style="left:911px">Contact</a>
</nav>

<div class="brand-oval">
  <span class="brand-mark"></span><span class="brand-name">Inn Riderz</span>
</div>

<section class="booking-panel">
  <h1 class="booking-title">Inn Riderz Booking</h1>
  <div class="booking-rule"></div>

  <span class="field-label" style="left:31px;top:85px">Select Country</span>
  <div class="select-box" style="left:31px;top:113px">Your Country<svg width="8" height="8" viewBox="0 0 8 8"><path d="M0 1h8L4 7z" fill="#fff"/></svg></div>
  <span class="field-label" style="left:252px;top:85px">Select City</span>
  <div class="select-box" style="left:252px;top:113px">Your city<svg width="8" height="8" viewBox="0 0 8 8"><path d="M0 1h8L4 7z" fill="#fff"/></svg></div>

  <span class="field-label" style="left:31px;top:170px">Arrival</span>
  <div class="check-box" style="left:31px;top:197px"></div>
  <span class="field-label" style="left:252px;top:170px">Departure</span>
  <div class="check-box" style="left:252px;top:197px"></div>

  <span class="field-label" style="left:31px;top:232px">Arrival Date</span>
  <div class="select-box" style="left:31px;top:259px">00-00-2012<svg width="8" height="8" viewBox="0 0 8 8"><path d="M0 1h8L4 7z" fill="#fff"/></svg></div>
  <span class="field-label" style="left:252px;top:232px">Arrival Time</span>
  <div class="select-box" style="left:252px;top:259px">00.00.00<svg width="8" height="8" viewBox="0 0 8 8"><path d="M0 1h8L4 7z" fill="#fff"/></svg></div>

  <span class="field-label" style="left:31px;top:322px">Airline</span>
  <div class="select-box" style="left:31px;top:350px">Airline select<svg width="8" height="8" viewBox="0 0 8 8"><path d="M0 1h8L4 7z" fill="#fff"/></svg></div>
  <span class="field-label" style="left:252px;top:322px">Airport</span>
  <div class="select-box" style="left:252px;top:350px">Airport select<svg width="8" height="8" viewBox="0 0 8 8"><path d="M0 1h8L4 7z" fill="#fff"/></svg></div>

  <span class="field-label" style="left:31px;top:410px">Hotel</span>
  <div class="select-box" style="left:31px;top:437px">Hotel select<svg width="8" height="8" viewBox="0 0 8 8"><path d="M0 1h8L4 7z" fill="#fff"/></svg></div>
  <div class="go-button">Go&gt;</div>

  <div class="panel-divider"></div>
  <span class="social-chip" style="left:18px"></span>
  <span class="social-chip" style="left:55px"></span>
  <span class="social-chip" style="left:92px"></span>
  <div class="phone-box">
    <svg width="20" height="20" viewBox="0 0 24 24"><path d="M6.6 10.8a15 15 0 0 0 6.6 6.6l2.2-2.2c.3-.3.7-.4 1-.2 1.1.4 2.3.6 3.6.6.6 0 1 .4 1 1V20c0 .6-.4 1-1 1A17 17 0 0 1 3 4c0-.6.4-1 1-1h3.5c.6 0 1 .4 1 1 0 1.3.2 2.5.6 3.6.1.3 0 .7-.2 1z" fill="#fff"/></svg>
    555-010-4477
  </div>
</section>

<section class="promo-panel">
  <h2 class="promo-title">Lorem ipsum dolar sit amit</h2>
  <div class="slide-arrows"><span>&#9664;</span><span>&#9654;</span></div>
  <div class="promo-photo" role="img" aria-label="Photo of a smiling woman in a sun hat waving from an open-top blue sports car"></div>
  <div class="slide-dots"><i class="on"></i><i></i><i></i><i></i><i></i></div>
  <p class="promo-copy" style="top:382px">Lowest prices-guaranteed Client Services &amp; Support Available 24/7 Unmatched Hotel Chauffeuring Experience 99.2% Client Satisfaction</p>
  <p class="promo-copy" style="top:489px">No fee for Cancels or Changes within 2 hours of services100% services Guarantee Your Services experi-ence is assured!! Flight Tracking Technology insures we are there to greet you! All INCLUSIVE PRICING-NO EXTRA FEES, NO SURPRISES</p>
</section>

<div class="newsletter">Type Your Email here</div>
<div class="subscribe-button">Subscribe</div>

<div class="footer-brand"><span class="brand-mark"></span><span class="brand-name">Inn Riderz</span></div>
<div class="copyright">Copyright 2012 Inn Riderz All Right Reserved</div>

</body>
</html>
```